Spark of Meadow Paddocks Business Cards with logo

Need a creative business card that pops. Colorful but professional. The attached logo should be included. We are a national horse racing partnership so we are in the equine business. Nothing cartoonlike or whimsical.

Target Market(s)

professionals - 40+

Contact Information for Business Card

Dana Whitlow
Director of Operations
27 Pinecrest Lane
Brookvale, MD. 20999

Phone (555) 274-6183

FX: (555) 619-3047

email: dana@smpaddocks.example
smpaddocks.example

Requirements
Must have
• All information above should be on the business card including the website address. Professional yet creative
Nice to have
• an attention grabbing design. not boring. exciting.
Should not have
• cartoon like - whimsical.

```html
<!DOCTYPE html>
<html lang="en">
<head>
<meta charset="utf-8">
<title>Spark of Meadow Paddocks — Business Cards</title>
<link href="https://fonts.googleapis.com/css2?family=Roboto:wght@400;700&display=swap" rel="stylesheet">
<style>
  :root {
    --navy: #2b2f7a;
    --gold: #c39a2c;
    --paper: #ffffff;
    --backdrop: #2a2a2e;
  }
  * { box-sizing: border-box; margin: 0; padding: 0; }
  html, body { width: 1200px; height: 800px; overflow: hidden; }
  body {
    background: var(--backdrop);
    font-family: "Roboto", Arial, sans-serif;
    color: var(--navy);
    position: relative;
  }
  .card {
    position: absolute;
    top: 250px;
    width: 525px;
    height: 300px;
    background: var(--paper);
    overflow: hidden;
  }
  .card--front { left: 50px; }
  .card--back { left: 625px; }

  .brand {
    display: flex;
    align-items: center;
    gap: 10px;
    font-weight: 700;
    color: var(--navy);
    text-transform: uppercase;
    letter-spacing: 2px;
    white-space: nowrap;
  }
  .brand__mark {
    width: 22px; height: 22px;
    border-radius: 50%;
    background: var(--gold);
    flex: none;
  }
  .card--front .brand {
    position: absolute;
    left: 0; right: 0; top: 138px;
    justify-content: center;
    font-size: 16px;
  }
  .card--back .brand {
    position: absolute;
    right: 30px; top: 40px;
    font-size: 12px;
    letter-spacing: 1.5px;
  }
  .card--back .brand__mark { width: 18px; height: 18px; }

  .person {
    position: absolute;
    left: 36px; top: 166px;
  }
  .person__name { font-size: 22px; font-weight: 700; line-height: 1.1; }
  .person__role { font-size: 12px; margin-top: 2px; }

  .rule {
    position: absolute;
    left: 36px; right: 20px; top: 212px;
    height: 1px;
    background: var(--gold);
  }
  .contacts {
    position: absolute;
    left: 36px; right: 20px; top: 224px;
    display: flex;
    align-items: center;
    font-size: 11.5px;
    line-height: 1.55;
  }
  .contacts__group { display: flex; flex-direction: column; }
  .contacts__divider {
    width: 1.5px; height: 30px;
    background: var(--gold);
    margin: 0 16px;
    flex: none;
  }
  .contacts__item { display: flex; align-items: center; gap: 7px; white-space: nowrap; }
  .contacts__line { white-space: nowrap; }
  .icon { width: 11px; height: 11px; flex: none; }
  .band {
    position: absolute;
    left: 0; right: 0; bottom: 0;
    height: 12px;
    background: var(--gold);
  }
</style>
</head>
<body>

  <section class="card card--front" aria-label="Card front">
    <div class="brand"><span class="brand__mark"></span>Spark of Meadow Paddocks</div>
  </section>

  <section class="card card--back" aria-label="Card back">
    <div class="brand"><span class="brand__mark"></span>Spark of Meadow Paddocks</div>

    <div class="person">
      <p class="person__name">Dana Whitlow</p>
      <p class="person__role">Director of Operations</p>
    </div>

    <div class="rule"></div>

    <div class="contacts">
      <div class="contacts__group">
        <span class="contacts__item">
          <svg class="icon" viewBox="0 0 24 24" fill="var(--gold)"><path d="M6.6 10.8a15.1 15.1 0 0 0 6.6 6.6l2.2-2.2a1 1 0 0 1 1-.25 11.4 11.4 0 0 0 3.6.57 1 1 0 0 1 1 1V20a1 1 0 0 1-1 1A17 17 0 0 1 3 4a1 1 0 0 1 1-1h3.5a1 1 0 0 1 1 1c0 1.25.2 2.450.57 3.57a1 1 0 0 1-.25 1z"/></svg>
          (555) 274-6183
        </span>
        <span class="contacts__item">
          <svg class="icon" viewBox="0 0 24 24" fill="var(--gold)"><path d="M6 2h12v6H6z"/><path d="M3 9h18v9h-3v4H6v-4H3zm5 6v5h8v-5z"/></svg>
          (555) 619-3047
        </span>
      </div>
      <span class="contacts__divider"></span>
      <div class="contacts__group">
        <span class="contacts__item">
          <svg class="icon" viewBox="0 0 24 24" fill="var(--gold)"><path d="M2 5h20v14H2zm2 2v.5l8 5 8-5V7l-8 5z"/></svg>
          dana@smpaddocks.example
        </span>
        <span class="contacts__item">
          <svg class="icon" viewBox="0 0 24 24" fill="none" stroke="var(--gold)" stroke-width="2"><circle cx="12" cy="12" r="9"/><path d="M3 12h18M12 3c3 3 3 15 0 18M12 3c-3 3-3 15 0 18"/></svg>
          smpaddocks.example
        </span>
      </div>
      <span class="contacts__divider"></span>
      <div class="contacts__group">
        <span class="contacts__line">27 Pinecrest Lane</span>
        <span class="contacts__line">Brookvale, MD. 20999</span>
      </div>
    </div>

    <div class="band"></div>
  </section>

</body>
</html>
```